TK AG Flyer design

I’d like to redesign an A5, double-sided flyer for the company TK AG (www.tkag.lu). The text/content is available in a Word document.

```html
<!DOCTYPE html>
<html lang="de">
<head>
<meta charset="utf-8">
<title>TK AG Flyer</title>
<link href="https://fonts.googleapis.com/css2?family=Montserrat:wght@400;500;600;700;800;900&family=Roboto+Condensed:wght@500;700&display=swap" rel="stylesheet">
<style>
:root{
  --orange:#f5a623;
  --navy:#1330a6;
  --ink:#1b1b22;
  --grey-text:#444;
  --paper:#ffffff;
  --stage:#8a8a8a;
}
*{margin:0;padding:0;box-sizing:border-box}
html,body{width:1200px;height:821px;overflow:hidden;background:var(--stage);font-family:"Montserrat",sans-serif;color:var(--ink)}
.page{position:absolute;top:82px;width:463px;height:656px;background:var(--paper);overflow:hidden}
.page--front{left:87px}
.page--back{left:650px}
.abs{position:absolute}
.brand{position:absolute;display:flex;align-items:center;gap:6px}
.brand__mark{width:14px;height:14px;background:var(--navy)}
.brand__name{font-weight:700;font-size:14px;color:var(--navy);line-height:1}
.headline{font-weight:900;line-height:.98;text-transform:uppercase}
.headline .o{color:var(--orange)}
.headline .n{color:var(--navy)}
.chip{display:inline-flex;align-items:center;gap:4px;background:var(--navy);color:#fff;font-weight:700;font-size:10px;padding:1px 7px 1px 3px;border-radius:10px}
.chip i,.pill i{display:inline-block;width:10px;height:10px;border-radius:50%;background:var(--orange);flex:none}
.pill{display:inline-flex;align-items:center;gap:6px;font-weight:700;color:#fff;border-radius:14px;padding:2px 12px 2px 4px}
.pill--orange{background:var(--orange);color:var(--navy)}
.pill--navy{background:var(--navy)}
.pill--orange i{background:var(--navy)}
.photo{position:absolute}
.list-item{font-size:8.6px;line-height:1.25;padding:7px 0 7px 9px;border-bottom:1px solid rgba(255,255,255,.35);position:relative}
.list-item::before{content:"";position:absolute;left:0;top:10px;width:5px;height:5px;border-radius:50%;background:var(--orange)}
.eff-item{font-size:8.6px;line-height:1.3;padding:7px 0 7px 9px;border-bottom:1px solid #bbb;color:var(--grey-text);position:relative}
.eff-item b{color:var(--ink)}
.eff-item::before{content:"";position:absolute;left:0;top:10px;width:5px;height:5px;border-radius:50%;background:var(--navy)}
.step{position:absolute;left:0;display:flex;align-items:center}
.step__num{width:40px;height:40px;border-radius:50%;background:#fff;border:3px solid var(--orange);display:flex;align-items:center;justify-content:center;font-family:"Roboto Condensed",sans-serif;font-weight:700;font-size:19px;color:var(--navy);position:relative;z-index:2;box-shadow:0 1px 3px rgba(0,0,0,.25);flex:none}
.step__text{margin-left:-10px;background:#fff;border-radius:0 13px 13px 0;height:26px;width:176px;padding-left:18px;display:flex;align-items:center;font-size:6.8px;line-height:1.2;color:#333}
.body-small{font-size:7.2px;line-height:1.3;color:var(--ink)}
.contact{position:absolute;display:flex;gap:10px;align-items:center;font-size:7.6px;color:var(--ink)}
.contact span::before{content:"";display:inline-block;width:6px;height:6px;border-radius:50%;background:var(--navy);margin-right:3px}
</style>
</head>
<body>

<section class="page page--front">
  <h1 class="headline abs" style="left:29px;top:30px;font-size:24px">
    <span class="o">Solarenergie</span><br><span class="n">Energieeffizienz</span>
  </h1>
  <div class="brand" style="left:330px;top:40px">
    <span class="brand__mark"></span><span class="brand__name">TK AG</span>
  </div>
  <p class="abs" style="left:29px;top:80px;font-size:12px">aus einer Hand Mehr Eigenverbrauch.</p>
  <div class="abs" style="left:29px;top:98px;display:flex;gap:6px">
    <span class="chip"><i></i>Mehr Effizienz</span><span class="chip"><i></i>Mehr Zukunft</span>
  </div>
  <p class="abs" style="left:29px;top:118px;font-size:11px;line-height:1.2;width:330px">Wir planen und beraten rund um Photovoltaik und Energieeffizienz – für</p>
  <p class="abs" style="left:29px;top:148px;font-size:11px;font-weight:600">
    <span style="color:var(--navy)">●</span> Private &nbsp;<span style="color:var(--navy)">●</span> Gewerbe &nbsp;<span style="color:var(--navy)">●</span> Industrie
  </p>

  <div class="photo" role="img" aria-label="Photo of a house roof with black solar panels and alpine landscape" style="left:0;top:178px;width:300px;height:200px;background:linear-gradient(180deg,#b9c7d2 0%,#7f8f6a 35%,#3a3f48 60%,#6d5a4c 100%)"></div>
  <div class="photo" role="img" aria-label="Cutaway illustration of a house with heating, solar and energy systems" style="left:209px;top:150px;width:244px;height:250px;background:linear-gradient(160deg,#f1ece6 0%,#d8d4cf 50%,#7a7470 85%,#3f4a2e 100%);clip-path:polygon(45% 0,100% 20%,100% 82%,55% 100%,0 80%,0 35%)"></div>

  <svg class="abs" style="left:0;top:240px" width="250" height="120" viewBox="0 0 250 120">
    <polygon points="0,60 0,80 60,120 90,120" fill="var(--orange)"/>
  </svg>

  <div class="abs" style="left:29px;top:282px;width:170px;height:292px;background:var(--navy);color:#fff;padding:32px 10px 0 10px">
    <span class="pill pill--orange" style="position:absolute;left:8px;top:2px;font-size:11px"><i></i>Solar Energie</span>
    <p style="font-size:9.6px;line-height:1.25;margin-bottom:6px">Photovoltaik-Lösungen, die zu Ihrem Dach passen</p>
    <div class="list-item"><b>Indach PV-Anlagen</b><br>(integriert &amp; ästhetisch)</div>
    <div class="list-item"><b>Aufdach PV-Anlagen</b><br>(effizient &amp; preis-/leistungsstark)</div>
    <div class="list-item" style="border:0"><b>Eigenverbrauch optimieren</b><br>(Batterie, Wärmepumpe,<br>E-Mobility, smartes<br>Lastmanagement)</div>
  </div>

  <div class="photo" role="img" aria-label="Photo of a white house with dark solar roof" style="left:0;top:514px;width:241px;height:142px;background:linear-gradient(170deg,#fff 0%,#9aa0a6 30%,#2e3238 60%,#d9d6d0 100%);clip-path:polygon(0 30%,70% 0,100% 20%,100% 100%,0 100%)"></div>

  <span class="pill pill--navy abs" style="left:253px;top:420px;font-size:11px"><i></i>Energie Effizienz</span>
  <p class="abs" style="left:253px;top:443px;font-size:9.6px;line-height:1.2;color:var(--grey-text)">Beratung &amp; Konzepte für<br>nachhaltige Gebäude</p>
  <div class="abs" style="left:253px;top:470px;width:200px">
    <div class="eff-item"><b>Energieberatung / GEAK / GEAK Plus</b></div>
    <div class="eff-item"><b>Impulsberatung &amp; Energiekonzept</b><br>(HLK + PV, Simulationen, Nachweise)</div>
    <div class="eff-item" style="border:0"><b>Energiesanierung</b> (Planung,<br>Koordination, Förderabwicklung)</div>
  </div>
  <p class="abs" style="left:253px;top:596px;font-family:'Roboto Condensed',sans-serif;font-weight:700;font-size:11px">Jetzt unverbindlich Kontakt aufnehmen</p>
  <div class="abs" style="left:230px;top:612px;display:flex;font-family:'Roboto Condensed',sans-serif;font-weight:700;font-size:9.5px">
    <span style="background:var(--orange);color:var(--ink);padding:2px 8px 2px 26px;border-radius:10px 0 0 10px">Telefon oder E-Mail</span>
    <span style="background:var(--navy);color:#fff;padding:2px 8px;border-radius:0 10px 10px 0">wir melden uns zeitnah</span>
  </div>
</section>

<section class="page page--back">
  <h2 class="headline abs" style="left:27px;top:30px;font-size:18.5px">
    <span class="o">Indach oder Aufdach?</span><br><span class="n">Wir finden die<br>passende Lösung</span>
  </h2>
  <div class="brand" style="left:360px;top:34px">
    <span class="brand__mark"></span><span class="brand__name" style="font-size:12px">TK AG</span>
  </div>
  <span class="pill pill--orange abs" style="left:29px;top:93px;font-size:11px;padding:1px 14px">Indach PV</span>
  <span class="pill pill--orange abs" style="left:205px;top:93px;font-size:11px;padding:1px 14px">Aufdach PV</span>
  <p class="abs body-small" style="left:29px;top:114px;width:165px"><b>Ist ideal bei Neubau oder Dachsanierung:</b> Module ersetzen die Dacheindeckung – funktional und optisch hochwertig</p>
  <p class="abs body-small" style="left:205px;top:114px;width:180px">Eignet sich besonders bei bestehenden Dächern in gutem Zustand – mit Standardmodulen oft die effizienteste Technologie zum besten Preis.</p>

  <div class="photo" role="img" aria-label="Photo of a tiled roof with black solar modules" style="left:0;top:162px;width:463px;height:166px;background:linear-gradient(160deg,#9fb0bf 0%,#6d6a5e 25%,#1f2329 50%,#2b2e34 75%,#a0593a 100%);clip-path:polygon(0 0,100% 0,100% 78%,72% 100%,40% 85%,0 75%)"></div>
  <svg class="abs" style="left:0;top:260px" width="463" height="120" viewBox="0 0 463 120">
    <polygon points="0,78 0,92 100,118 120,118" fill="var(--orange)"/>
    <polygon points="330,60 463,90 463,106 330,76" fill="var(--orange)"/>
  </svg>

  <div class="abs" style="left:274px;top:300px;width:189px;height:274px;background:var(--navy);clip-path:polygon(40% 0,100% 8%,100% 100%,0 100%,0 4%)"></div>
  <p class="abs" style="left:290px;top:340px;color:#fff;font-weight:700;font-size:11px;line-height:1.2">So läuft<br>die Zusammenarbeit</p>
  <div class="abs" style="left:254px;top:374px;width:209px;height:230px">
    <div class="step" style="top:0"><span class="step__num">01</span><span class="step__text">Erstkontakt (Telefon/E-Mail)</span></div>
    <div class="step" style="top:46px"><span class="step__num">02</span><span class="step__text">Analyse / Check vor Ort (Daten,<br>Bedarf, Potenziale)</span></div>
    <div class="step" style="top:92px"><span class="step__num">03</span><span class="step__text">Konzept, Wirtschaftlichkeit<br>&amp; Massnahmenplan</span></div>
    <div class="step" style="top:138px"><span class="step__num">04</span><span class="step__text">Umsetzung mit<br>eingespieltem Partnernetzwerk</span></div>
    <div class="step" style="top:184px"><span class="step__num">05</span><span class="step__text"><span><b style="color:var(--navy)">Optional:</b> Monitoring &amp; Wartung<br>für dauerhaft hohe Leistung</span></span></div>
  </div>

  <span class="pill pill--navy abs" style="left:28px;top:312px;font-size:10.5px;line-height:1.1;padding:3px 12px 3px 4px"><i></i>Eigenverbrauch<br>erhöhen</span>
  <p class="abs body-small" style="left:29px;top:349px;width:230px">Rendite steigern: Viele PV-Anlagen produzieren mehr Strom, als gleichzeitig benötigt wird. Mit passenden Massnahmen erhöhen Sie Ihren Eigenverbrauch – z. B. durch Batteriesysteme, Wärmepumpen-Ansteuerung, überschussvariables Laden von E-Fahrzeugen oder gezieltes Schalten von Verbrauchern.</p>

  <span class="pill pill--orange abs" style="left:28px;top:430px;font-size:10.5px;line-height:1.1;padding:3px 12px 3px 4px"><i></i>Energieberatung<br>&amp; Sanierung</span>
  <p class="abs body-small" style="left:29px;top:467px;width:230px">ganzheitlich gedacht Wir analysieren Ihr Gebäude, erstellen einen Sanierungs- und Effizienzplan und unterstützen bei Bewilligungen und Fördergeldern – bis zur Umsetzung und Abnahme.</p>
  <div class="photo" role="img" aria-label="Photo of technicians at a building installation" style="left:28px;top:528px;width:94px;height:74px;border-radius:6px;border:2px solid var(--navy);background:linear-gradient(160deg,#c9d4dc,#7b8a8f 60%,#d07a30)"></div>
  <div class="photo" role="img" aria-label="Photo of a heat pump and storage tanks in a technical room" style="left:128px;top:528px;width:94px;height:74px;border-radius:6px;border:2px solid var(--navy);background:linear-gradient(160deg,#d6d8da,#8d9295 60%,#5b6064)"></div>

  <div class="abs" style="left:0;top:622px;width:463px;height:34px;background:linear-gradient(180deg,#fcc24a,var(--orange))"></div>
  <div class="abs" style="left:35px;top:612px;width:393px;height:22px;background:#fff;border-radius:11px;border:1px solid var(--orange)"></div>
  <div class="contact" style="left:47px;top:618px">
    <span>+41 41 555 01 20</span><span>info@tkag.lu</span><span>Seeblickstrasse 12, CH-6000 Luzern</span><span>www.tkag.lu</span>
  </div>
</section>

</body>
</html>
```